Nu Upsilon civil engineering orgnization activities flyer

we need flyer design for Nu Upsilon civil engineering honor society in University of Brenmoor for science and technology. the flyer contain the schedule of the expected activity. the design should have a purple color and Nu Upsilon Key and logo (you will find them in the attached file) and the design should have something referring to civil engineering

Industry/Entity Type

Education

Colors
6b449b

Requirements
Must have
• Nu Upsilon logo, key, motto
Nice to have
• civil engineering samples, purple color

```html
<!DOCTYPE html>
<html lang="en">
<head>
<meta charset="utf-8">
<title>Nu Upsilon – Activities Flyer</title>
<link href="https://fonts.googleapis.com/css2?family=Cinzel:wght@700&family=Montserrat:wght@800&family=Open+Sans:ital,wght@0,400;0,700;1,700&display=swap" rel="stylesheet">
<style>
  :root {
    --purple: #6b449b;
    --purple-dark: #3f2363;
    --purple-mid: #563480;
    --lavender: #e6e1ee;
    --gold: #d6b23c;
    --ink: #111;
    --white: #fff;
  }
  html, body { margin: 0; padding: 0; overflow: hidden; background: var(--white); }
  .flyer {
    position: relative; width: 848px; height: 1200px; overflow: hidden;
    background: var(--white); font-family: "Open Sans", Arial, sans-serif; color: var(--ink);
  }
  .header { position: absolute; left: 0; top: 0; width: 848px; height: 175px; }
  .header svg { position: absolute; inset: 0; }
  .header-mark {
    position: absolute; left: 46px; top: 16px; width: 46px; height: 46px;
    border-radius: 50%; background: var(--gold);
  }
  .header-title {
    position: absolute; left: 110px; top: 14px; margin: 0;
    font-family: "Cinzel", Georgia, serif; font-size: 64px; line-height: 1; color: var(--white);
    letter-spacing: 1px;
  }
  .header-subtitle {
    position: absolute; left: 258px; top: 100px; margin: 0;
    font-size: 17px; color: #d9d0e6;
  }
  .header-pillars {
    position: absolute; left: 592px; top: 20px; width: 244px; margin: 0;
    font-family: "Cinzel", Georgia, serif; color: var(--white); line-height: 1.1;
    white-space: nowrap;
  }
  .header-pillars span { display: block; font-size: 27px; }
  .header-pillars span.strong { font-size: 27px; }
  .motto {
    position: absolute; left: 12px; top: 170px; width: 824px; margin: 0;
    text-align: center; font-size: 14.5px; font-weight: 700; font-style: italic; line-height: 1.35;
  }
  .skyline {
    position: absolute; left: 600px; top: 240px; width: 248px; height: 697px;
    background: linear-gradient(180deg, #fff 0%, var(--lavender) 45%, #f1eef6 100%);
    opacity: .8;
  }
  .portrait {
    position: absolute; left: 604px; top: 384px; width: 244px; height: 816px;
    background: linear-gradient(180deg, #caa58f 0%, #3a3a44 18%, #1f1f26 60%, #2a2a30 100%);
    border-radius: 110px 110px 0 0; z-index: 3;
  }
  .section-title {
    position: absolute; left: 8px; margin: 0;
    font-size: 29px; font-weight: 700; color: var(--purple); line-height: 1;
  }
  .schedule {
    position: absolute; left: 8px; top: 246px; width: 582px;
    border-collapse: collapse; font-size: 15.5px; z-index: 2; background: var(--white);
  }
  .schedule th, .schedule td {
    border: 1.5px solid var(--ink); text-align: left; vertical-align: top;
    padding: 2px 6px; line-height: 1.3;
  }
  .schedule td { height: 22px; }
  .schedule th { color: var(--purple); font-weight: 700; height: 40px; }
  .schedule col.no { width: 94px; } .schedule col.date { width: 101px; }
  .schedule col.time { width: 63px; } .schedule col.loc { width: 84px; }
  .schedule col.name { width: 129px; }
  .block { position: absolute; left: 8px; width: 560px; margin: 0; font-size: 14px; line-height: 1.45; z-index: 2; }
  .block.justify { text-align: justify; }
  .block b { font-weight: 700; }
  .contact-band {
    position: absolute; left: 0; top: 937px; width: 848px; height: 146px;
    background: linear-gradient(90deg, var(--purple-dark), var(--purple) 70%, var(--purple-mid));
  }
  .contact {
    position: absolute; left: 8px; top: 948px; margin: 0; z-index: 2;
    font-family: "Montserrat", Arial, sans-serif; font-weight: 800; color: var(--white);
    font-size: 16.5px; line-height: 1.52;
  }
  .footer-name {
    position: absolute; left: 14px; top: 1110px; display: flex; align-items: center; gap: 12px;
    font-family: "Cinzel", Georgia, serif; font-size: 46px; color: var(--purple);
  }
  .footer-name i { width: 34px; height: 34px; border-radius: 50%; background: var(--gold); display: block; }
  .footer-badge {
    position: absolute; left: 470px; top: 1092px; width: 110px; display: flex; flex-direction: column; align-items: center; gap: 6px;
    font-size: 13px; font-weight: 700; color: var(--ink);
  }
  .footer-badge i { width: 62px; height: 62px; background: var(--purple); display: block; }
</style>
</head>
<body>
<div class="flyer">
  <header class="header">
    <svg width="848" height="175" viewBox="0 0 848 175">
      <defs>
        <linearGradient id="headerFill" x1="0" y1="0" x2="1" y2="0">
          <stop offset="0" stop-color="#3f2363"/>
          <stop offset="0.55" stop-color="#6b449b"/>
          <stop offset="1" stop-color="#4a2b70"/>
        </linearGradient>
      </defs>
      <polygon points="0,0 848,0 848,128 0,165" fill="url(#headerFill)"/>
    </svg>
    <span class="header-mark"></span>
    <h1 class="header-title">NU UPSILON</h1>
    <p class="header-subtitle">The Civil Engineering Honor Society</p>
    <p class="header-pillars"><span>Conception</span><span>Design</span><span class="strong">Construction</span></p>
  </header>

  <p class="motto">Nu Upsilon retains as its motto the Greek letters Nu Delta Nu, which formed the name of the junior honor society founded in 1922 at the University of Calverton and which is one of the roots of Nu Upsilon.</p>

  <div class="skyline" role="img" aria-label="Faint line sketch of city skyscrapers"></div>
  <div class="portrait" role="img" aria-label="Photo of a smiling young engineer in a dark suit and striped tie"></div>

  <h2 class="section-title" style="top:214px">Meeting</h2>
  <table class="schedule">
    <colgroup><col class="no"><col class="date"><col class="time"><col class="loc"><col class="name"><col></colgroup>
    <thead>
      <tr><th>Meeting No.</th><th>Date</th><th>Time</th><th>Location</th><th>Name</th><th>Company</th></tr>
    </thead>
    <tbody>
      <tr><td>1</td><td>9/8/2015</td><td>7 PM</td><td>BCH 124</td><td>Dr. Hartwell</td><td></td></tr>
      <tr><td>2</td><td>9/22/2015</td><td>7 PM</td><td>BCH 124</td><td>Reggie Moreland</td><td>Metro Utilities</td></tr>
      <tr><td>3</td><td>10/6/2015</td><td>7 PM</td><td>BCH 124</td><td>Mark Danforth</td><td>Ft. Ashgrove</td></tr>
      <tr><td>4</td><td>10/20/2015</td><td>7 PM</td><td>BCH 124</td><td>Taylor Brennick</td><td>Vexa Inc.</td></tr>
      <tr><td>5</td><td>11/3/2015</td><td>7 PM</td><td>BCH 124</td><td>Scavenger Hunt</td><td>Social</td></tr>
      <tr><td>6</td><td>11/17/2015</td><td>7 PM</td><td>BCH 124</td><td>Nomination/ Ron Keplar</td><td>Harlow Wealth</td></tr>
      <tr><td>7</td><td>12/1/2015</td><td>7 PM</td><td>BCH 124</td><td>Elections</td><td>-</td></tr>
    </tbody>
  </table>

  <h2 class="section-title" style="top:538px">Service</h2>
  <p class="block justify" style="top:569px">
    <b>Greer Conservation Area Service Day</b> / Saturday, Oct 24, 11 am / Greer Conservation Area, Millbrook, MO 65499, United States<br>
    <b>Civic Partnership Service Day</b> / Saturday, Nov 7, 11 am / The Civic Partnership Resale Shop, 2400 N Aldridge Ave, Millbrook, MO 65499, United States<br>
    <b>Tri Valley Humane Society Volunteer Day</b> / Thursday, Nov 12, 12 pm / Tri Valley Humane Society, 812 E Fairview St, Oak Hollow, MO 65598, United States
  </p>

  <h2 class="section-title" style="top:704px">Social</h2>
  <p class="block" style="top:735px; line-height:1.7">
    Nu Upsilon Smoker<br>
    Bowling / Lanternlite Lanes (1420 Crown Highway)/ Wednesday, October 28th /9:00 PM<br>
    Plaque Signing/ When: December 8th / the Zone
  </p>

  <h2 class="section-title" style="top:838px">Initiation</h2>
  <p class="block" style="top:869px; line-height:1.65">
    12/12/2015 &nbsp;&nbsp;&nbsp; 5 PM-6PM &nbsp;&nbsp;&nbsp; BCH 314<br>
    6:30PM initiation diner / Marlow's- 1300 North Carver Street, Oak Hollow,
  </p>

  <div class="contact-band"></div>
  <p class="contact">
    University of Brenmoor for science and technology<br>
    PO Box 48207<br>
    Brenmoor, TX 76500-0412<br>
    555.014.2290 (PH) • 555.014.7781 (FAX)<br>
    nuhq@brenmoor.edu • www.nu-upsilon.org
  </p>

  <div class="footer-name"><i></i>NU UPSILON</div>
  <div class="footer-badge">NU UPSILON<i></i></div>
</div>
</body>
</html>
```